Tidewell Pronto Clinic Business card

We want a business card that matches our business theme. Our website is www.prontoclinicbz.example
The company name is Tidewell Pronto Clinic
The persons having the business cards will be doctors
My logo is attached.
We have a drive-thru medical center where our motto is Fast, Reliable, and Convenient. Our goal is to change the medical space while utilizing technologies, keeping a professional and clean look

Medical

Info on the card should be: Name, Position, Cell number, website, email address, possibly the office line as well

• Logo
• Professional medical feel with our logo colors incorporated

```html
<!DOCTYPE html>
<html lang="en">
<head>
<meta charset="utf-8">
<title>Tidewell Pronto Clinic – Business Card</title>
<link href="https://fonts.googleapis.com/css2?family=Questrial&display=swap" rel="stylesheet">
<style>
  :root{
    --royal:#17469e;
    --navy:#1a3f98;
    --sky:#33c3ef;
    --ink:#2b2b2b;
    --paper:#ffffff;
    --stage:#e6e8ec;
    --mist:#e9eef7;
  }
  *{margin:0;padding:0;box-sizing:border-box}
  html,body{width:1200px;height:874px;overflow:hidden}
  body{background:var(--stage);font-family:"Questrial",sans-serif;position:relative}
  .card{position:absolute;left:260px;width:680px;height:388px;overflow:hidden;box-shadow:0 6px 18px rgba(0,0,0,.18)}
  .card--front{top:34px;background:var(--royal)}
  .card--back{top:452px;background:var(--paper)}

  /* front */
  .front-mark{position:absolute;left:0;right:0;top:120px;display:flex;align-items:center;justify-content:center;gap:18px}
  .front-mark__dot{width:58px;height:58px;border-radius:50%;border:7px solid var(--sky)}
  .front-mark__name{color:var(--paper);font-size:34px;letter-spacing:.5px}
  .front-url{position:absolute;left:0;right:0;bottom:62px;text-align:center;color:var(--paper);font-size:15px;letter-spacing:7px}

  /* back */
  .back-halo{position:absolute;left:-70px;top:10px;width:330px;height:330px;border-radius:50%;background:var(--mist)}
  .brand{position:absolute;right:40px;top:34px;text-align:right}
  .brand__row{display:flex;align-items:center;gap:12px;justify-content:flex-end}
  .brand__name{color:var(--navy);font-size:30px;line-height:1.05}
  .brand__dot{width:52px;height:52px;border-radius:50%;border:6px solid var(--navy)}
  .person{position:absolute;left:52px;top:150px}
  .person__name{color:var(--navy);font-size:26px}
  .person__role{color:var(--sky);font-size:15px;margin-top:2px}
  .rule{position:absolute;left:52px;right:40px;top:212px;height:1.5px;background:var(--sky)}
  .contacts{position:absolute;left:52px;top:228px;list-style:none;color:var(--ink);font-size:15px;line-height:22px}
  .contacts li{display:flex;align-items:center;gap:9px}
  .contacts svg{width:12px;height:12px;fill:var(--navy)}
  .address{position:absolute;right:40px;bottom:58px;text-align:right;color:var(--ink);font-size:16px;line-height:20px}
  .band{position:absolute;bottom:0;height:20px}
  .band--sky{left:0;width:300px;background:var(--sky)}
  .band--navy{left:300px;right:0;background:var(--navy)}
</style>
</head>
<body>
  <section class="card card--front">
    <div class="front-mark">
      <span class="front-mark__dot"></span>
      <span class="front-mark__name">Tidewell Pronto Clinic</span>
    </div>
    <p class="front-url">www.prontoclinicbz.example</p>
  </section>

  <section class="card card--back">
    <div class="back-halo"></div>
    <div class="brand">
      <div class="brand__row">
        <span class="brand__name">Tidewell<br>Pronto Clinic</span>
        <span class="brand__dot"></span>
      </div>
    </div>
    <div class="person">
      <p class="person__name">Marlon-Keith D.r</p>
      <p class="person__role">Site Manager</p>
    </div>
    <div class="rule"></div>
    <ul class="contacts">
      <li><svg viewBox="0 0 24 24"><path d="M6.6 10.8a15.1 15.1 0 0 0 6.6 6.6l2.2-2.2a1 1 0 0 1 1-.25 11.4 11.4 0 0 0 3.6.57 1 1 0 0 1 1 1V20a1 1 0 0 1-1 1A17 17 0 0 1 3 4a1 1 0 0 1 1-1h3.5a1 1 0 0 1 1 1c0 1.25.2 2.45.57 3.57a1 1 0 0 1-.25 1z"/></svg>(501)-555-0148</li>
      <li><svg viewBox="0 0 24 24"><path d="M2 5h20v14H2z M2 5l10 8 10-8" /></svg>info@prontoclinicbz.example</li>
      <li><svg viewBox="0 0 24 24"><circle cx="12" cy="12" r="10"/></svg>www.prontoclinicbz.example</li>
    </ul>
    <p class="address">42 Harbourview Lane<br>Belmopan Belize</p>
    <div class="band band--sky"></div>
    <div class="band band--navy"></div>
  </section>
</body>
</html>
```